Lawn Company needs design work on a service call flyer!

We are a lawn care company that fertilizes and sprays lawns. This design is meant to be left behind at the customers house after a lawn application has been done too let them know what we have done.

The finished design will be printed on A6 paper (4.1 x 5.8 inches)

I have attached PDF files of the text that I want on the front of the document and the back of the document. I also included a sample design that I had been working on to give some idea what I would like. I don't want the same design, but you can use it as a building block for something new or come up with something entirely different.

FRONT: The front of the design is most important.

BACK: Other then the text the design should be minimal. If possible I would like an outline of the trees in my logo to be a backdrop. I have attached a PDF of the back of my business card as an example

The winning design will be a professional looking document that flows and reflects a lawn care business. Please contact me if you have any questions. I will only pick a design that is better then my current template.

Thank You

Target Market(s)

Lawn Care Customers

Industry/Entity Type

Lawn Care

Requirements
Must have
• 1. Our Logo
• 2. The attached text for the front & back of document
• 3. Our phone number (604-918-4471)
• 4. Our Email address (fenwickturfcare@mailora.net)
Nice to have
• A green theme with flowing graphics
Should not have
• any pictures of houses, people, or tools
• Don't copy the text or design from my design template. It is outdated, is it meant to be an example only

```html
<!DOCTYPE html>
<html lang="en">
<head>
<meta charset="utf-8">
<title>Fenwick Turf Care – Service Call Flyer</title>
<link rel="stylesheet" href="https://fonts.googleapis.com/css2?family=Roboto+Condensed:wght@400;700&family=Arimo:wght@700&display=swap">
<style>
  :root {
    --canvas-bg: #e9ece9;
    --paper: #ffffff;
    --leaf-green: #5cb446;
    --brand-green: #4a9a3a;
    --deep-green: #1d5c3a;
    --slate-green: #4e6b5e;
    --clay-red: #c9605a;
    --ink: #222222;
    --grass-light: #7cc24f;
    --grass-dark: #2f6b2a;
  }
  html, body {
    margin: 0;
    padding: 0;
    width: 1200px;
    height: 1200px;
    overflow: hidden;
    background: var(--canvas-bg);
  }
  .canvas {
    position: relative;
    width: 1200px;
    height: 1200px;
  }
  .flyer {
    position: absolute;
    left: 204px;
    top: 40px;
    width: 918px;
    height: 1297px;
    background: var(--paper);
    transform: scale(0.8635);
    transform-origin: 0 0;
    box-shadow: 0 6px 18px rgba(0,0,0,0.25);
    overflow: hidden;
    font-family: "Roboto Condensed", "Arial Narrow", sans-serif;
    color: var(--ink);
  }
  .flyer__art {
    position: absolute;
    inset: 0;
    width: 918px;
    height: 1297px;
  }
  .brand {
    position: absolute;
    left: 55px;
    top: 250px;
    width: 400px;
    text-align: center;
    font-weight: 700;
    color: var(--brand-green);
    line-height: 1;
  }
  .brand__name {
    display: block;
    font-size: 64px;
    letter-spacing: 2px;
  }
  .brand__tagline {
    display: block;
    font-size: 30px;
    letter-spacing: 5px;
    margin-top: 6px;
  }
  .contact {
    position: absolute;
    left: 45px;
    top: 390px;
    width: 420px;
    text-align: center;
    font-size: 28px;
    line-height: 37px;
  }
  .field {
    position: absolute;
    font-size: 25px;
    white-space: nowrap;
  }
  .blank {
    display: inline-block;
    border-bottom: 1.5px solid var(--ink);
    height: 22px;
    vertical-align: baseline;
  }
  .field--date { left: 379px; top: 553px; }
  .field--date .blank { width: 238px; }
  .field--tech { left: 30px; top: 624px; }
  .field--tech .blank { width: 222px; }
  .applied__title {
    position: absolute;
    left: 30px;
    top: 692px;
    margin: 0;
    font-family: "Arimo", Arial, sans-serif;
    font-weight: 700;
    font-size: 26px;
    color: var(--deep-green);
  }
  .applied__list {
    position: absolute;
    left: 78px;
    top: 765px;
    margin: 0;
    padding: 0;
    list-style: none;
    font-size: 25px;
  }
  .applied__list li {
    position: relative;
    padding-left: 25px;
    height: 71px;
  }
  .applied__list li::before {
    content: "";
    position: absolute;
    left: 2px;
    top: 12px;
    width: 9px;
    height: 9px;
    border-radius: 50%;
    background: var(--ink);
  }
  .applied__list .blank { width: 560px; }
  .field--water { left: 30px; top: 979px; }
  .field--water .blank { width: 348px; margin: 0 4px; }
  .pledge {
    position: absolute;
    left: 27px;
    top: 1163px;
    width: 863px;
    margin: 0;
    color: #ffffff;
    font-size: 22px;
    line-height: 30px;
    text-align: justify;
  }
</style>
</head>
<body>
<main class="canvas">
  <article class="flyer">
    <svg class="flyer__art" viewBox="0 0 918 1297" xmlns="http://www.w3.org/2000/svg">
      <defs>
        <linearGradient id="lawnScene" x1="0" y1="0" x2="0" y2="1">
          <stop offset="0" stop-color="#4f8a3a"/>
          <stop offset="0.45" stop-color="#2f6b2a"/>
          <stop offset="0.75" stop-color="#6bb443"/>
          <stop offset="1" stop-color="#8ccc55"/>
        </linearGradient>
      </defs>
      <g class="header-photo" role="img" aria-label="Photo of a freshly mowed striped lawn with trees and a backyard patio">
        <path d="M0,0 H918 V380 C650,340 250,180 0,165 Z" fill="url(#lawnScene)"/>
      </g>
      <path class="wave wave--green" d="M0,165 C250,180 650,340 918,380 V448 C650,430 300,250 0,235 Z" fill="var(--leaf-green)"/>
      <path class="wave wave--red" d="M0,235 C300,250 650,430 918,448 V478 C650,460 300,272 0,260 Z" fill="var(--clay-red)"/>
      <circle class="badge" cx="255" cy="350" r="208" fill="var(--paper)"/>
      <path class="badge__ring" d="M52,395 A208,208 0 0 0 460,385" fill="none" stroke="var(--leaf-green)" stroke-width="6"/>
      <path class="footer-wave footer-wave--green" d="M0,1050 C250,1028 560,1050 918,1165 V1297 H0 Z" fill="var(--leaf-green)"/>
      <path class="footer-wave footer-wave--red" d="M0,1116 C250,1068 600,1074 918,1165 V1297 H0 Z" fill="var(--clay-red)"/>
      <path class="footer-wave footer-wave--slate" d="M0,1155 C260,1090 600,1085 918,1180 V1297 H0 Z" fill="var(--slate-green)"/>
    </svg>

    <div class="brand">
      <span class="brand__name">FENWICK</span>
      <span class="brand__tagline">TURF CARE</span>
    </div>

    <div class="contact">
      CONTACT US : 604-918-4471<br>
      fenwickturfcare@mailora.net
    </div>

    <div class="field field--date">APPLICATION TIME / DATE:<span class="blank"></span></div>
    <div class="field field--tech">YOUR LAWN HAS BEEN PROFFESIONALLY SERVICED TODAY BY<span class="blank"></span></div>

    <h2 class="applied__title">Today's application consists of</h2>
    <ul class="applied__list">
      <li>Seasonally Balanced Slow Release Fertilizer</li>
      <li>Broadleaf Weed Control (Please keep off the lawn until it is thoroughly dry)</li>
      <li>Other <span class="blank"></span></li>
    </ul>

    <div class="field field--water">Please begin watering the lawn <span class="blank"></span> after application</div>

    <p class="pledge">“We strive to complete work in a professional manner each and every visit. If you are not satisfied with the level of service you are receiving please contact us. We value your business and wish to maintain long-term relationships with our customers.”</p>
  </article>
</main>
</body>
</html>
```